Bref créative
Business Cards and Stationery Project
Verdant Pathways Health and Fitness Center
I need double sided standard sized Business Card [3.5" x 2"]
Use same fonts as used on my logo but also try different fonts
Professional
Marcus T. Delaney
Owner/Health Practitioner
4172 Larchmont Ave S
Minneapolis, MN 55405
marcus.delaney@vpwellbody.com
www.vpwellbody.com
Looking for a clean looking business card/stationery. It would be nice to have health center tagline w/ company name one one side. Tagline Where optimum health is your greatest wealth. If possible can there be date and time space for appointment.

```html
<!DOCTYPE html>
<html lang="en">
<head>
<meta charset="utf-8">
<title>Verdant Pathways Stationery</title>
<link href="https://fonts.googleapis.com/css2?family=Open+Sans:wght@400;600;700&display=swap" rel="stylesheet">
<style>
:root{
  --bg:#ece7df;
  --paper:#ffffff;
  --blue:#1f5fa8;
  --blue-deep:#123f7a;
  --green:#7cc242;
  --green-deep:#4f9a2a;
  --ink:#555b60;
  --label:#7a726a;
  --faint:#e6eef3;
}
*{margin:0;padding:0;box-sizing:border-box}
html,body{width:1200px;height:446px;overflow:hidden}
body{background:var(--bg);font-family:"Open Sans",sans-serif;color:var(--ink);position:relative}
.piece{position:absolute;background:var(--paper);box-shadow:0 2px 6px rgba(0,0,0,.18);overflow:hidden}
.label{position:absolute;font-size:6px;letter-spacing:.12em;text-transform:uppercase;color:var(--label)}
.brand{position:absolute;text-align:center;line-height:1.1}
.brand-name{font-weight:700;color:var(--blue);font-size:9px;letter-spacing:.04em;display:flex;align-items:center;gap:3px;justify-content:center}
.brand-name .dot{width:5px;height:5px;border-radius:50%;background:var(--green)}
.brand-sub{font-size:4px;color:var(--green-deep);letter-spacing:.05em}
.swoosh{position:absolute;left:0;top:0}
.watermark{position:absolute;border-radius:50%;background:radial-gradient(circle,var(--faint) 0%,rgba(230,238,243,0) 70%)}
.contact{position:absolute;font-size:4px;line-height:1.5;color:var(--ink)}
/* business card */
.card-front{left:12px;top:168px;width:137px;height:72px}
.card-back{left:12px;top:246px;width:137px;height:78px}
.card-back .heading{position:absolute;left:8px;top:8px;font-size:4.5px;font-weight:600;color:var(--blue)}
.card-back .line{position:absolute;left:8px;right:8px;height:0;border-bottom:.6px solid #b9c3cb;font-size:4px}
.card-back .line span{position:absolute;bottom:1px;left:0}
.card-back .band{position:absolute;left:0;right:0;bottom:0;height:8px;background:linear-gradient(90deg,var(--blue),var(--green))}
/* letterheads */
.letterhead{top:12px;width:288px;height:408px}
.lh-1{left:168px}
.lh-2{left:475px}
/* envelopes */
.envelope{left:773px;width:417px}
.env-blue{top:10px;height:106px;background:linear-gradient(180deg,var(--blue-deep),var(--blue) 60%,#3d82c8)}
.env-green{top:122px;height:118px}
.env-green .flap{position:absolute;left:0;right:0;top:0;height:52px;background:linear-gradient(180deg,var(--green-deep),var(--green))}
.env-white{top:262px;height:132px}
</style>
</head>
<body>

<div class="label" style="left:12px;top:156px">Business Card Fronts</div>
<section class="piece card-front">
  <svg class="swoosh" width="137" height="72" viewBox="0 0 137 72"><path d="M0 0H40Q15 10 0 26Z" fill="var(--blue)"/><path d="M0 26Q15 10 40 0H48Q20 12 0 32Z" fill="var(--green)"/></svg>
  <div class="brand" style="left:26px;top:14px;width:100px"><div class="brand-name"><span class="dot"></span>Verdant Pathways</div><div class="brand-sub">Health and Fitness Center</div></div>
  <div class="contact" style="left:10px;top:38px">Marcus T. Delaney<br>Owner/Health Practitioner<br>4172 Larchmont Ave S, Minneapolis, MN 55405<br>marcus.delaney@vpwellbody.com · www.vpwellbody.com</div>
</section>
<section class="piece card-back">
  <div class="heading">Where optimum health is your greatest wealth</div>
  <div class="line" style="top:28px"><span>Appointment for</span></div>
  <div class="line" style="top:42px"><span>Date</span></div>
  <div class="line" style="top:56px"><span>Time</span></div>
  <div class="band"></div>
</section>
<div class="label" style="left:12px;top:332px">Business Card Back</div>

<section class="piece letterhead lh-1">
  <svg class="swoosh" width="288" height="60" viewBox="0 0 288 60"><path d="M0 0H110Q40 18 0 48Z" fill="var(--blue)"/><path d="M0 48Q40 18 110 0H126Q50 24 0 58Z" fill="var(--green)"/></svg>
  <div class="brand" style="left:150px;top:22px;width:120px"><div class="brand-name"><span class="dot"></span>Verdant Pathways</div><div class="brand-sub">Health and Fitness Center</div></div>
  <div class="watermark" role="img" aria-label="Faint brand emblem watermark" style="left:84px;top:150px;width:120px;height:130px"></div>
  <div class="contact" style="left:22px;top:370px">Marcus T. Delaney<br>4172 Larchmont Ave S, Minneapolis, MN 55405<br>marcus.delaney@vpwellbody.com<br>www.vpwellbody.com</div>
</section>
<div class="label" style="left:270px;top:430px">Letterhead Option 1</div>

<section class="piece letterhead lh-2">
  <svg class="swoosh" width="288" height="60" viewBox="0 0 288 60"><path d="M0 0H110Q40 18 0 48Z" fill="var(--blue)"/><path d="M0 48Q40 18 110 0H126Q50 24 0 58Z" fill="var(--green)"/></svg>
  <div class="brand" style="left:150px;top:22px;width:120px"><div class="brand-name"><span class="dot"></span>Verdant Pathways</div><div class="brand-sub">Health and Fitness Center</div></div>
  <div class="watermark" role="img" aria-label="Faint brand emblem watermark" style="left:84px;top:150px;width:120px;height:130px"></div>
  <div class="contact" style="left:0;right:0;top:385px;text-align:center">4172 Larchmont Ave S, Minneapolis, MN 55405 · marcus.delaney@vpwellbody.com · www.vpwellbody.com</div>
</section>
<div class="label" style="left:577px;top:430px">Letterhead Option 2</div>

<section class="piece envelope env-blue"></section>
<section class="piece envelope env-green"><div class="flap"></div><div class="brand" style="left:188px;top:70px;width:40px"><div class="brand-name"><span class="dot"></span></div></div></section>
<section class="piece envelope env-white">
  <svg class="swoosh" width="417" height="40" viewBox="0 0 417 40"><path d="M0 0H90Q30 12 0 30Z" fill="var(--blue)"/><path d="M0 30Q30 12 90 0H102Q38 16 0 36Z" fill="var(--green)"/></svg>
  <div class="brand" style="left:18px;top:42px;width:110px;text-align:left"><div class="brand-name" style="justify-content:flex-start"><span class="dot"></span>Verdant Pathways</div><div class="brand-sub">4172 Larchmont Ave S, Minneapolis, MN 55405</div></div>
</section>
<div class="label" style="left:940px;top:406px">Envelope Design</div>

</body>
</html>
```